Paper Harbour Services Flyer

Create a 2 sided A4 flyer/PDF of the services we offer and a description of each etc.
Details can be found at: https://www.paper-harbour.co.uk/
Main services: Document Scanning, Invoice Processing and other services we offer.

Industry/Entity Type

Document Management

Font styles to use
Other font styles liked:
• Montserrat

Colors

Designer to choose colors to be used in the design.

Requirements
Must have
• Document Scanning, Box Storage, Invoice Processing, Book Scanning, Large format scanning
Nice to have
• Colourful d/s flyer listing our services with a brief description on each

```html
<!DOCTYPE html>
<html lang="en">
<head>
<meta charset="utf-8">
<title>Paper Harbour – Services Flyer</title>
<link rel="stylesheet" href="https://fonts.googleapis.com/css2?family=Bebas+Neue&family=Montserrat:wght@400;600;700&display=swap">
<style>
  :root {
    --backdrop: #636363;
    --red: #d0202a;
    --navy: #1d4a63;
    --paper: #f1f2f4;
    --paper-light: #fbfbfc;
    --ink: #1a1a1a;
    --white: #ffffff;
    --photo-warm: #c9b9a6;
    --machine: #d8d9db;
  }
  * { box-sizing: border-box; margin: 0; padding: 0; }
  html, body { width: 1200px; height: 859px; overflow: hidden; background: var(--backdrop); }
  body { position: relative; font-family: "Montserrat", sans-serif; color: var(--ink); }

  .page {
    position: absolute; top: 82px; width: 491px; height: 694px; overflow: hidden;
    background:
      linear-gradient(135deg, transparent 0 38%, rgba(255,255,255,.7) 38% 46%, transparent 46%),
      linear-gradient(225deg, transparent 0 30%, rgba(255,255,255,.6) 30% 40%, transparent 40%),
      linear-gradient(180deg, var(--paper-light), var(--paper));
  }
  .page--front { left: 86px; }
  .page--back { left: 623px; }

  .abs { position: absolute; }

  /* Front hero */
  .hero-title { left: 40px; top: 40px; font-family: "Bebas Neue", sans-serif; font-size: 59px; line-height: 49px; color: var(--navy); letter-spacing: .2px; font-weight: 400; }
  .hero-title .accent { color: var(--red); }
  .hero-intro { left: 40px; top: 202px; width: 205px; font-size: 9px; line-height: 10.6px; font-weight: 600; }
  .hero-panel { left: 259px; top: 42px; width: 232px; height: 215px; }
  .hero-machine { left: 312px; top: 58px; width: 156px; height: 190px; border-radius: 6px; background: linear-gradient(180deg, #2b2b2b 0 30%, var(--machine) 30% 70%, #b7bcc0 70%); opacity: .9; }

  /* Service bands */
  .band { left: 0; top: 286px; width: 491px; height: 325px; }
  .band--red { background: linear-gradient(100deg, var(--red), #c51d26 70%, #b81c24); }
  .band--navy { background: linear-gradient(100deg, var(--navy), #1a4259 70%, #183d52); }

  .service-title { font-size: 16px; line-height: 19px; font-weight: 600; color: var(--white); }
  .service-text { font-size: 7.3px; line-height: 11px; color: var(--white); text-align: justify; width: 285px; }
  .service-text + .service-text { margin-top: 11px; }

  .photo-frame { width: 122px; border: 1.3px solid var(--white); border-radius: 9px; padding: 4px; }
  .photo { width: 100%; height: 100%; border-radius: 6px; }

  /* Footer */
  .brand-name { left: 40px; top: 641px; font-size: 17px; line-height: 20px; font-weight: 600; color: var(--red); white-space: nowrap; }
  .call-panel { left: 210px; top: 625px; width: 281px; height: 51px; }
  .call-line { right: 29px; top: 628px; font-family: "Bebas Neue", sans-serif; font-size: 23px; line-height: 26px; color: var(--white); white-space: nowrap; }
  .call-address { right: 29px; top: 656px; font-size: 7px; line-height: 9.3px; color: var(--white); text-align: right; white-space: nowrap; }

  /* Back page top */
  .facility-panel { left: 31px; top: 18px; width: 460px; height: 115px; }
  .facility-title { left: 52px; top: 26px; font-size: 16px; font-weight: 700; color: var(--white); }
  .facility-text { color: var(--white); font-size: 7.3px; line-height: 11px; text-align: justify; }
  .machine-shot { border-radius: 4px; }
</style>
</head>
<body>

<!-- Front -->
<section class="page page--front">
  <h1 class="abs hero-title">Document<br><span class="accent">Automation</span><br>Services</h1>
  <p class="abs hero-intro">At Paper Harbour, we deliver award-winning document automation services, from business process optimisation and document management to data capture and document scanning.</p>

  <svg class="abs hero-panel" viewBox="0 0 232 215" aria-hidden="true">
    <path d="M22 0 H232 V215 H72 Q58 215 53 201 L3 24 Q-2 0 22 0 Z" fill="var(--navy)"/>
  </svg>
  <div class="abs hero-machine" role="img" aria-label="Overhead book scanner workstation on a desk with a monitor"></div>

  <div class="abs band band--red"></div>

  <h2 class="abs service-title" style="left:39px;top:300px;">Document Scanning</h2>
  <p class="abs service-text" style="left:39px;top:320px;">Paper Harbour provides high-quality document scanning services tailored to businesses of all sizes. Whether you're looking to digitise a single department's files or undertake a large-scale bulk scanning project, our state-of-the-art technology and expertise ensure exceptional results. We specialise in scanning in PDF format, preserving fragile materials, and offering solutions like A3 scanning and microfilm digitisation. Our efficient process transforms paper archives into accessible, organised digital records, unlocking the full potential of your business information. By converting physical documents into digital formats, we help businesses streamline workflows, save space, and improve access to important information. Our services are designed to support organisations across sectors, delivering customised solutions to meet unique requirements.</p>
  <div class="abs photo-frame" style="left:341px;top:306px;height:150px;">
    <div class="photo" role="img" aria-label="Operator feeding documents into a production scanner" style="background:linear-gradient(135deg,#e9d9cf,var(--photo-warm) 50%,#5d6c78);"></div>
  </div>

  <h2 class="abs service-title" style="left:39px;top:469px;">Archive Box Storage Solutions</h2>
  <div class="abs" style="left:39px;top:494px;">
    <p class="service-text">Trust Paper Harbour for secure and efficient box storage and document storage services. For over 40 years, we have provided secure offsite document storage solutions tailored to businesses needing to declutter their offices while still maintaining easy access to archived records at any time.</p>
    <p class="service-text">Our advanced online inventory system provides a fully searchable list of your stored boxes, enabling effortless monitoring and retrieval. Request box returns, scanning services, or secure shredding through our dedicated team of professionals.</p>
  </div>
  <div class="abs photo-frame" style="left:341px;top:471px;height:121px;">
    <div class="photo" role="img" aria-label="Stacked grey archive storage boxes" style="background:linear-gradient(160deg,#d6d6d6,#8d8d8d 55%,#4a4a4a);"></div>
  </div>

  <div class="abs brand-name">Paper Harbour</div>
  <svg class="abs call-panel" viewBox="0 0 281 51" aria-hidden="true">
    <path d="M10 0 H281 V51 H30 Q21 51 18 42 L2 11 Q-2 0 10 0 Z" fill="var(--navy)"/>
  </svg>
  <div class="abs call-line">Call now today! 01632 960418</div>
  <div class="abs call-address">Paper Harbour Ltd Harbour House,<br>Quayside Way, Northgate, West Sussex RH99 1ZZ</div>
</section>

<!-- Back -->
<section class="page page--back">
  <svg class="abs facility-panel" viewBox="0 0 460 115" aria-hidden="true">
    <path d="M12 0 H460 V115 H40 Q31 115 28 106 L1 13 Q-2 0 12 0 Z" fill="var(--red)"/>
  </svg>
  <h2 class="abs facility-title">4 Secure Production Facilities</h2>
  <p class="abs facility-text" style="left:53px;top:54px;width:408px;">Founded in 1989 we provided archival services to microfilm. Today we are a processing powerhouse, focused on feeding the systems which drive your business.</p>
  <p class="abs facility-text" style="left:61px;top:87px;width:400px;">Registered under the Data Protection Act and compliant to the UK General and Data Protection Regulation, Paper Harbour are a reliable and secure service provider. Our Quality Management Systems and Information Security Management systems are independently accredited to International Standards.</p>

  <div class="abs machine-shot" role="img" aria-label="High-volume desktop document scanner" style="left:34px;top:166px;width:172px;height:90px;background:linear-gradient(90deg,#222 0 30%,#efefef 30%);"></div>
  <div class="abs machine-shot" role="img" aria-label="Overhead book scanning workstation" style="left:196px;top:162px;width:86px;height:100px;background:linear-gradient(180deg,#2b2b2b 0 35%,var(--machine) 35%);"></div>
  <div class="abs machine-shot" role="img" aria-label="Large production scanning machine with monitor" style="left:297px;top:160px;width:162px;height:107px;background:linear-gradient(180deg,#e4e4e4,#b9bbbe);"></div>

  <div class="abs band band--navy"></div>

  <h2 class="abs service-title" style="left:29px;top:308px;font-size:16.5px;line-height:21px;">Streamline Supplier Invoice<br>Processing with Automation</h2>
  <div class="abs" style="left:29px;top:354px;">
    <p class="service-text">In today’s fast-paced business environment, time is money. Yet, many companies still rely on manual processes for managing supplier invoices – processes that are slow, error-prone, and difficult to track. Implementing invoice automation transforms these manual steps into streamlined workflows, empowering your team to focus on strategic tasks and reducing operational inefficiencies.</p>
    <p class="service-text">Our AP automation services eliminate the need for slow, manual data entry by automatically extracting key information from supplier invoices. This data is validated for accuracy and seamlessly integrated into your invoicing system and ERP platforms, enabling smooth processing and reporting.</p>
  </div>
  <div class="abs photo-frame" style="left:338px;top:306px;height:150px;">
    <div class="photo" role="img" aria-label="Person reviewing an invoice on a computer monitor" style="background:linear-gradient(120deg,#e8e3da,#c7c9cc 55%,#f3f3f3);"></div>
  </div>

  <h2 class="abs service-title" style="left:29px;top:497px;font-size:16.5px;line-height:18px;">Book Scanning<br>Services</h2>
  <p class="abs service-text" style="left:29px;top:538px;">At Paper Harbour, our book scanning services are designed to deliver high-quality digital reproductions of your books while ensuring the utmost care for the original materials. Whether your project involves scanning a single rare volume or digitising an entire library, we employ advanced, non-destructive methods that cater to the specific needs of your collection.</p>
  <div class="abs photo-frame" style="left:338px;top:471px;height:121px;">
    <div class="photo" role="img" aria-label="Person scanning an open book on an overhead scanner" style="background:linear-gradient(120deg,#d9c8b4,#eae7e2 55%,#9a9da0);"></div>
  </div>

  <div class="abs brand-name">Paper Harbour</div>
  <svg class="abs call-panel" viewBox="0 0 281 51" aria-hidden="true">
    <path d="M10 0 H281 V51 H30 Q21 51 18 42 L2 11 Q-2 0 10 0 Z" fill="var(--navy)"/>
  </svg>
  <div class="abs call-line">Call now today! 01632 960418</div>
  <div class="abs call-address">Paper Harbour Ltd Harbour House,<br>Quayside Way, Northgate, West Sussex RH99 1ZZ</div>
</section>

</body>
</html>
```